PowerPoint Template Design for business consulting company in Silicon Valley

I need a PowerPoint template to use as the starting point for new presentations. I have a logo but now need design that supports this. I've attached a very descriptive PDF that explains exactly what I need. Here is a list of deliverables: 1. PowerPoint Template that I will use as the starter presentation for all new Lantern Quorix presentationsDesigns for the following slides: See picture below for examples of structure:2. Title slide with subtitle3. Section header4. Title and body5. Title and 2 columns6. Title and 3 columns7. One column text8. Editable timeline to show months, or steps for a process9. Bullet design for unordered list (can be graphic)10. Bullet design for ordered list11. Recommended fonts for each design: Title, subtitle, list, captionOPTIONAL: Possible graphic elements to be used for section title slide backgrounds or graphic elements:--Your team / my team / people on project--Goals for project / presentation--Editable Timeline--Speaking--Writing--Listening--People collaborating / helping each otherI am happy to accept proposals for developing these optional elements in a separate project.

Requirements
Must have
• Must be FLAT design.
• Not flashy or garish. Must be subtle.

```html
<!DOCTYPE html>
<html lang="en">
<head>
<meta charset="utf-8">
<title>Lantern Quorix – Presentation Template</title>
<link rel="stylesheet" href="https://fonts.googleapis.com/css2?family=Alegreya+Sans:wght@400;500&family=Tinos&display=swap">
<style>
  :root{
    --page:#c3c3c3;
    --paper:#ffffff;
    --green:#1f7a35;
    --green-bright:#3aa64a;
    --green-dark:#17652b;
    --blue:#1c3f98;
    --blue-mid:#2a78c0;
    --teal:#137a80;
    --grey:#9a9a9a;
    --text:#333333;
    --rule:#dcdcdc;
    --mist:#ececec;
  }
  *{box-sizing:border-box;margin:0;padding:0}
  html,body{width:1200px;height:1200px;overflow:hidden;background:var(--page)}
  body{position:relative;font-family:"Tinos",serif;color:var(--text)}
  .slide{position:absolute;width:377px;height:212px;background:var(--paper);overflow:hidden}
  .col-1{left:27px}.col-2{left:414px}.col-3{left:802px}
  .row-1{top:247px}.row-2{top:475px}.row-3{top:702px}

  .scenery{position:absolute;right:0;bottom:0;width:70%;height:80%;
    background:radial-gradient(ellipse at 85% 85%, var(--mist) 0%, rgba(236,236,236,.6) 35%, rgba(255,255,255,0) 70%)}
  .bar-left{position:absolute;left:0;top:0;width:18px;height:100%;
    background:linear-gradient(180deg,var(--blue) 0%,var(--teal) 50%,var(--green-bright) 100%)}
  .bar-right{position:absolute;right:19px;top:0;width:19px;height:100%;
    background:linear-gradient(180deg,var(--green-bright) 0%,var(--teal) 50%,var(--blue) 100%)}

  .title{position:absolute;left:31px;top:21px;font-family:"Alegreya Sans",sans-serif;font-size:15px;color:var(--green);white-space:nowrap}
  .title-rule{position:absolute;left:30px;right:0;top:44px;border-top:1px dotted var(--rule)}
  .heading{position:absolute;font-family:"Tinos",serif;font-size:10px;color:var(--green);white-space:nowrap}
  .body{position:absolute;font-size:5.6px;line-height:10.4px;text-align:justify;color:var(--text)}

  .badge{position:absolute;right:10px;top:7px;width:32px;height:32px;border-radius:50%;border:1px solid var(--green);
    display:flex;align-items:center;justify-content:center;text-align:center;
    font-family:"Alegreya Sans",sans-serif;font-size:5px;line-height:5.5px;color:var(--blue)}

  /* title slide */
  .hero{position:absolute;left:0;top:0;width:100%;height:130px;
    background:linear-gradient(100deg,#2b56a6 0%,#2a7d8c 50%,#3aa64a 100%)}
  .hero-mark{position:absolute;left:149px;top:30px;width:80px;height:80px;border-radius:50%;border:2px solid #fff;
    display:flex;align-items:center;justify-content:center;text-align:center;
    font-family:"Alegreya Sans",sans-serif;font-size:13px;line-height:14px;color:#fff}
  .cover-title{position:absolute;left:0;width:100%;top:148px;text-align:center;font-family:"Alegreya Sans",sans-serif;font-size:22px;color:var(--green)}
  .cover-sub{position:absolute;left:0;width:100%;top:180px;text-align:center;font-family:"Alegreya Sans",sans-serif;font-size:10.5px;color:var(--blue)}
  .swoosh{position:absolute;left:0;top:150px}

  .section-box{position:absolute;left:54px;top:88px;width:260px;height:38px;border:1px dotted var(--rule);
    text-align:center;font-family:"Alegreya Sans",sans-serif;font-size:21px;line-height:36px;color:var(--green)}
  .text-box{position:absolute;left:26px;top:63px;width:333px;height:105px;border:1px dotted var(--rule);padding:5px 7px;font-size:6px}

  /* timeline */
  .tl-line{position:absolute;left:18px;right:0;top:66px;border-top:1.5px solid var(--blue)}
  .tl-stem{position:absolute;width:1px}
  .tl-dot{position:absolute;width:6px;height:6px;border-radius:50%;top:63px}
  .tl-year{position:absolute;width:26px;height:26px;border-radius:50%;color:#fff;font-size:7px;line-height:26px;text-align:center}
  .tl-head{position:absolute;font-size:6px;white-space:nowrap}
  .tl-text{position:absolute;width:52px;font-size:4.2px;line-height:5.6px;text-align:justify;background:var(--paper)}

  /* lists */
  .list-head{position:absolute;left:32px;font-size:10px;color:var(--blue)}
  .list{position:absolute;left:24px;font-size:6px;line-height:11px;list-style:none}
  .list li{position:relative;padding-left:8px}
  .list li::before{position:absolute;left:0;top:0;font-size:5px;color:var(--blue)}
  .list.bullets li::before{content:"";top:4px;width:4px;height:4px;border-radius:50%;border:.7px solid var(--grey)}
  .list.numbers{counter-reset:n}
  .list.numbers li{counter-increment:n}
  .list.numbers li::before{content:counter(n)}
</style>
</head>
<body>

<!-- Title slide -->
<section class="slide col-1 row-1">
  <div class="hero" role="img" aria-label="Blue to green photographic banner of bamboo leaves and lotus flowers"></div>
  <div class="hero-mark">Lantern<br>Quorix</div>
  <svg class="swoosh" width="90" height="40" viewBox="0 0 90 40"><path d="M0 28 Q40 -6 82 14 Q45 4 0 34 Z" fill="var(--green-bright)"/></svg>
  <div class="cover-title">Click to add title</div>
  <div class="cover-sub">Click to add subtitle</div>
</section>

<!-- Section header -->
<section class="slide col-2 row-1">
  <div class="scenery" role="img" aria-label="Faint grey bamboo backdrop"></div>
  <div class="bar-right"></div>
  <div class="section-box">Click to add title</div>
</section>

<!-- Title and body -->
<section class="slide col-3 row-1">
  <div class="scenery" role="img" aria-label="Faint grey bamboo backdrop"></div>
  <div class="bar-left"></div>
  <div class="title">Click to add title</div>
  <div class="title-rule"></div>
  <div class="badge">Lantern<br>Quorix</div>
  <div class="text-box">Click to add text</div>
</section>

<!-- Two columns -->
<section class="slide col-1 row-2">
  <div class="scenery" role="img" aria-label="Faint grey bamboo backdrop"></div>
  <div class="bar-left"></div>
  <div class="title">Click to add title</div>
  <div class="title-rule"></div>
  <div class="badge">Lantern<br>Quorix</div>
  <div class="heading" style="left:48px;top:56px">Click to add heading</div>
  <p class="body" style="left:47px;top:72px;width:126px">Lorem ipsum dolor sit amet, consectetuer adipiscing elit, sed diam nonummy nibh euismod tincidunt ut laoreet dolore magna aliquam erat volutpat. Ut wisi enim ad minim veniam, quis nostrud exerci tation ullamcorper suscipit lobortis nisl ut aliquip ex ea commodo consequat. Duis autem vel eum iriure dolor in hendrerit in vulputate velit esse molestie consequat, vel illum</p>
  <div class="heading" style="left:201px;top:56px">Click to add heading</div>
  <p class="body" style="left:200px;top:72px;width:126px">Lorem ipsum dolor sit amet, consectetuer adipiscing elit, sed diam nonummy nibh euismod tincidunt ut laoreet dolore magna aliquam erat volutpat. Ut wisi enim ad minim veniam, quis nostrud exerci tation ullamcorper suscipit lobortis nisl ut aliquip ex ea commodo consequat. Duis autem vel eum iriure dolor in hendrerit in vulputate velit esse molestie consequat, vel illum</p>
</section>

<!-- Three columns -->
<section class="slide col-2 row-2">
  <div class="scenery" role="img" aria-label="Faint grey bamboo backdrop"></div>
  <div class="bar-left"></div>
  <div class="title">Click to add title</div>
  <div class="title-rule"></div>
  <div class="badge">Lantern<br>Quorix</div>
  <div class="heading" style="left:27px;top:52px">Click to add heading</div>
  <p class="body" style="left:26px;top:67px;width:101px">Lorem ipsum dolor sit amet, consectetuer adipiscing elit, sed diam nonummy nibh euismod tincidunt ut laoreet dolore magna aliquam erat volutpat. Ut wisi enim ad minim veniam, quis nostrud exerci tation ullamcorper suscipit lobortis nisl ut aliquip ex ea commodo consequat. Duis autem vel eum iriure dolor in hendrerit in vulpu-</p>
  <div class="heading" style="left:142px;top:52px">Click to add heading</div>
  <p class="body" style="left:141px;top:67px;width:101px">Lorem ipsum dolor sit amet, consectetuer adipiscing elit, sed diam nonummy nibh euismod tincidunt ut laoreet dolore magna aliquam erat volutpat. Ut wisi enim ad minim veniam, quis nostrud exerci tation ullamcorper suscipit lobortis nisl ut aliquip ex ea commodo consequat. Duis autem vel eum iriure dolor in hendrerit in vulpu-</p>
  <div class="heading" style="left:257px;top:52px">Click to add heading</div>
  <p class="body" style="left:256px;top:67px;width:101px">Lorem ipsum dolor sit amet, consectetuer adipiscing elit, sed diam nonummy nibh euismod tincidunt ut laoreet dolore magna aliquam erat volutpat. Ut wisi enim ad minim veniam, quis nostrud exerci tation ullamcorper suscipit lobortis nisl ut aliquip ex ea commodo consequat. Duis autem vel eum iriure dolor in hendrerit in vulpu-</p>
</section>

<!-- One column -->
<section class="slide col-3 row-2">
  <div class="scenery" style="left:0;right:auto" role="img" aria-label="Faint grey bamboo backdrop"></div>
  <div class="bar-right" style="right:0"></div>
  <div class="heading" style="left:25px;top:40px">Click to add heading</div>
  <p class="body" style="left:24px;top:56px;width:126px">Lorem ipsum dolor sit amet, consectetuer adipiscing elit, sed diam nonummy nibh euismod tincidunt ut laoreet dolore magna aliquam erat volutpat. Ut wisi enim ad minim veniam, quis nostrud exerci tation ullamcorper suscipit lobortis nisl ut aliquip ex ea commodo consequat. Duis autem vel eum iriure dolor in hendrerit in vulputate velit esse molestie consequat, vel illum dolore eu feugiat nulla facilisis at vero eros et accumsan et iusto odio dignissim qui</p>
</section>

<!-- Title only -->
<section class="slide col-1 row-3">
  <div class="scenery" role="img" aria-label="Faint grey bamboo backdrop"></div>
  <div class="bar-left"></div>
  <div class="title">Click to add title</div>
  <div class="title-rule"></div>
  <div class="badge">Lantern<br>Quorix</div>
</section>

<!-- Timeline -->
<section class="slide col-2 row-3">
  <div class="scenery" role="img" aria-label="Faint grey bamboo backdrop"></div>
  <div class="bar-left"></div>
  <div class="title">Click to add title</div>
  <div class="badge">Lantern<br>Quorix</div>
  <div class="tl-line"></div>

  <!-- 2011 -->
  <div class="tl-stem" style="left:81px;top:66px;height:72px;background:var(--blue)"></div>
  <div class="tl-dot" style="left:78px;background:var(--blue)"></div>
  <div class="tl-year" style="left:68px;top:138px;background:var(--blue)">2011</div>
  <div class="tl-head" style="left:33px;top:78px;color:var(--blue)">heading</div>
  <p class="tl-text" style="left:21px;top:86px">Lorem ipsum dolor sit amet, consectetuer adipiscing elit, sed diam nonummy nibh euismod tincidunt ut laoreet dolore magna aliquam erat volutpat. Ut wisi enim ad</p>

  <!-- 2012 -->
  <div class="tl-stem" style="left:126px;top:66px;height:18px;background:var(--blue-mid)"></div>
  <div class="tl-dot" style="left:123px;background:var(--blue-mid)"></div>
  <div class="tl-year" style="left:113px;top:84px;background:var(--blue-mid)">2012</div>
  <div class="tl-head" style="left:117px;top:113px;color:var(--blue-mid)">heading</div>
  <p class="tl-text" style="left:101px;top:121px">Lorem ipsum dolor sit amet, consectetuer adipiscing elit, sed diam nonummy nibh euismod tincidunt ut laoreet dolore magna aliquam erat volutpat. Ut wisi enim ad minim</p>

  <!-- 2013: stem stops above the heading and resumes below the text -->
  <div class="tl-stem" style="left:184px;top:66px;height:17px;background:var(--green-dark)"></div>
  <div class="tl-stem" style="left:184px;top:139px;height:25px;background:var(--green-dark)"></div>
  <div class="tl-dot" style="left:181px;background:var(--green-dark)"></div>
  <div class="tl-year" style="left:171px;top:164px;background:var(--green-dark)">2013</div>
  <div class="tl-head" style="left:175px;top:84px;color:var(--green-dark)">heading</div>
  <p class="tl-text" style="left:159px;top:92px">Lorem ipsum dolor sit amet, consectetuer adipiscing elit, sed diam nonummy nibh euismod tincidunt ut laoreet dolore magna aliquam erat volutpat. Ut wisi enim ad minim</p>

  <!-- 2014 -->
  <div class="tl-stem" style="left:226px;top:66px;height:70px;background:var(--green-bright)"></div>
  <div class="tl-dot" style="left:223px;background:var(--green-bright)"></div>
  <div class="tl-year" style="left:213px;top:136px;background:var(--green-bright)">2014</div>
  <div class="tl-head" style="left:233px;top:73px;color:var(--green-bright)">heading</div>
  <p class="tl-text" style="left:233px;top:81px">Lorem ipsum dolor sit amet, consectetuer adipiscing elit, sed diam nonummy nibh euismod tincidunt ut laoreet dolore magna aliquam erat volutpat. Ut wisi enim ad minim</p>

  <!-- 2012 grey -->
  <div class="tl-stem" style="left:298px;top:66px;height:17px;background:var(--grey)"></div>
  <div class="tl-dot" style="left:295px;background:var(--grey)"></div>
  <div class="tl-year" style="left:285px;top:83px;background:var(--grey)">2012</div>
  <div class="tl-head" style="left:315px;top:73px;color:var(--grey)">heading</div>
  <p class="tl-text" style="left:315px;top:81px">Lorem ipsum dolor sit amet, consectetuer adipiscing elit, sed diam nonummy nibh euismod tincidunt ut laoreet dolore magna aliquam erat volutpat. Ut wisi enim ad minim</p>
</section>

<!-- Lists -->
<section class="slide col-3 row-3">
  <div class="scenery" role="img" aria-label="Faint grey bamboo backdrop"></div>
  <div class="bar-left"></div>
  <div class="title">Click to add title</div>
  <div class="badge">Lantern<br>Quorix</div>
  <div class="list-head" style="top:59px">Unordered list</div>
  <ul class="list bullets" style="top:75px">
    <li>Lorem ipsum dolor sit amet, consectetur adipiscing elit.</li>
    <li>Donec gravida massa ut arcu accumsan, ac hendrerit augue dapibus.</li>
    <li>Ut elementum ipsum vitae finibus mollis.</li>
    <li>Quisque vitae magna auctor nulla lacinia faucibus at gravida ante.</li>
  </ul>
  <div class="list-head" style="top:126px">Ordered list</div>
  <ol class="list numbers" style="top:142px">
    <li>Lorem ipsum dolor sit amet, consectetur adipiscing elit.</li>
    <li>Donec gravida massa ut arcu accumsan, ac hendrerit augue dapibus.</li>
    <li>Ut elementum ipsum vitae finibus mollis.</li>
    <li>Quisque vitae magna auctor nulla lacinia faucibus at gravida ante.</li>
  </ol>
</section>

</body>
</html>
```